Web site for Life Coaching Consultant

I require a website for a life coaching business. I have a Velvo Hosting account which I set up last week. I will need to be able to add articles and testimonials. The design should communicate that KT Amber Lantern is there to help people breakdown personal barriers and that we are an advocate to help them achieve personal goals.
Updates

Reason: I have some designers just accepting my invitation to submit so to give them a few days to submit. I have been thrilled with the quality of the submissions Thank you.

Hi everyone

I am loving all your designs.  The only feedback I can get from people is that they feel that the runner makes the web page look like a personal coach rather than a life coach that helps people with relations, career, and personal road blocks.

Sorry                                   

Reason: Hi I have increased the deadline as there has been so many amazing designs and some of you have asked to fine tune your entries. I would like to take this opportunity to thank you all. It is going to be a tough decision. I have put a few more pictures on the project page hoping this will help

Hi I just wanted to thank you all for your great designs.  As I got so many good designs I have asked people to vote.  I will be in touch in the next day or 2.

Cheers

Target Market(s)

People with self esteem issues either woman or girls, people who want to goal set and need an advocate

Industry/Entity Type

Life Coaching

Colors
d2a4cc
e567a6

Requirements
Must have
• must have bio section, logo, articles page, affirmation section and testimonial page.

```html
<!DOCTYPE html>
<html lang="en">
<head>
<meta charset="utf-8">
<title>KT Amber Lantern – Life Coaching</title>
<link href="https://fonts.googleapis.com/css2?family=Source+Sans+3:wght@400;600;700&family=Alfa+Slab+One&family=Russo+One&family=Arimo:wght@400;700&display=swap" rel="stylesheet">
<style>
:root{
  --page:#e6e6e6;
  --panel:#ffffff;
  --side:#333333;
  --side-line:#444444;
  --pink:#e0267a;
  --pink-soft:#e567a6;
  --red:#d9342b;
  --blue:#3b6f9a;
  --green:#2a7a1e;
  --ink:#222222;
  --muted:#666666;
  --light-text:#dddddd;
  --box-top:#ffffff;
  --box-bottom:#e2e2e2;
  --box-line:#d2d2d2;
}
*{box-sizing:border-box;margin:0;padding:0}
html,body{width:1200px;height:1099px;overflow:hidden}
body{position:relative;background:var(--page);font-family:"Source Sans 3",sans-serif;color:var(--ink)}
.abs{position:absolute}
.backdrop,.sidebar-shape{position:absolute;left:0;top:0}
.brand{left:110px;top:160px;width:240px;display:flex;align-items:center;justify-content:center;gap:8px}
.brand-dot{width:18px;height:18px;border-radius:50%;background:var(--pink);flex:none}
.brand-name{color:var(--pink);font-weight:700;font-size:23px;line-height:1}
.nav{left:124px;top:279px;width:212px;list-style:none;border-top:1px solid var(--side-line)}
.nav li{height:48px;border-bottom:1px solid var(--side-line);display:flex;align-items:center;padding-left:4px;color:#cfcfcf;font-size:19px;font-weight:400}
.nav li.active{color:#fff;font-weight:600}
.nav li::before{content:"";width:10px;height:10px;border:1px solid #bbb;border-radius:50%;margin-right:11px;background:radial-gradient(circle,#bbb 25%,transparent 30%)}
.side-title{color:var(--pink);font-size:22px;font-weight:600;line-height:1}
.contact{left:120px;top:579px;width:230px;list-style:none;color:var(--light-text);font-size:13px}
.contact li{display:flex;gap:10px;margin-bottom:7px;line-height:20px}
.contact svg{flex:none;margin-top:3px}
.contact a{color:var(--light-text)}
.widget{left:118px;top:836px;width:165px;color:var(--light-text);font-size:13px;line-height:20px}
.social{left:120px;top:926px;display:flex;gap:6px}
.social span{width:24px;height:24px;border-radius:50%;background:#555}
.hero{left:413px;top:68px;width:618px;height:279px;border-radius:60% 60% 0 0/12px 12px 0 0;background:linear-gradient(180deg,#6aa9d4 0%,#8cc0e0 55%,#3f8fb8 80%,#2b6f96 100%);overflow:hidden}
.hero-caption{left:425px;top:246px;width:420px;height:82px;background:rgba(255,255,255,.45);border-radius:4px;font-family:"Alfa Slab One",serif}
.hero-caption .l1{position:absolute;left:10px;top:12px;font-size:20px;color:var(--pink)}
.hero-caption .l1 b{color:#3aa0d8;font-weight:400}
.hero-caption .l2{position:absolute;left:56px;top:40px;font-size:29px;color:var(--blue)}
.hero-caption .l2 small{font-size:20px}
.dots{left:980px;top:333px;display:flex;gap:3px}
.dots span{width:10px;height:10px;background:#ddd}
.dots span.on{background:var(--pink)}
.box{background:linear-gradient(180deg,var(--box-top),var(--box-bottom));border:1px solid var(--box-line);border-radius:4px}
.quote{left:412px;top:366px;width:620px;height:120px}
.quote .mark{position:absolute;font-family:Georgia,serif;font-size:48px;color:#5b9bd0;line-height:1}
.quote .r1{position:absolute;left:60px;top:16px;font-size:30px;color:var(--blue);line-height:1.2}
.quote .r1 em{font-family:"Alfa Slab One",serif;font-style:normal;color:var(--red);letter-spacing:2px;margin-right:8px}
.quote .r2{position:absolute;left:32px;top:66px;font-size:24px;color:var(--pink);letter-spacing:1px;line-height:1.2}
.quote .r2 em{font-family:"Russo One",sans-serif;font-style:normal;color:var(--green);letter-spacing:1px;font-size:26px}
.about{left:412px;top:497px;width:619px;height:243px}
.portrait{position:absolute;background:linear-gradient(160deg,#b9a48d,#6c5a4c 60%,#2e2a28)}
.about .who{position:absolute;left:10px;top:106px;font-size:13px;color:#777;font-weight:600}
.about .who small{display:block;font-size:11px;margin-top:-2px}
.about .who small b{color:#3aa7d8}
.about h2{position:absolute;left:134px;top:4px;font-weight:400;font-size:29px}
.about h2 span,.articles h2 span{color:var(--pink)}
.about .lead{position:absolute;left:134px;top:48px;font-family:Arimo,sans-serif;font-size:12px;color:var(--red)}
.about .body{position:absolute;left:134px;top:76px;width:475px;font-family:Arimo,sans-serif;font-size:12.5px;line-height:20px;text-align:justify}
.more{font-weight:700;color:#444}
.more::after{content:" ⟶"}
.articles{left:413px;top:750px;width:319px;height:243px}
.articles h2{position:absolute;left:10px;top:10px;font-weight:400;font-size:30px}
.post{position:absolute;left:5px;width:308px;height:80px}
.post .date{position:absolute;left:0;top:0;width:52px;height:70px;background:linear-gradient(#fafafa,#ddd);border:1px solid #ddd;text-align:center;line-height:1}
.post .date b{display:block;font-size:28px;margin-top:6px}
.post .date span{font-size:26px;color:#444}
.post .txt{position:absolute;left:60px;top:0;width:248px;font-size:12px;line-height:18px;color:#444}
.sep{position:absolute;left:5px;top:137px;width:308px;border-top:1px dotted #bbb}
.testi-title{left:753px;top:748px;font-size:30px;font-weight:400}
.testi{left:753px;top:788px;width:279px;height:101px;border-radius:2px;text-align:center;font-family:Arimo,sans-serif;font-size:11.5px;line-height:14px;letter-spacing:.3px;padding:5px 8px;color:#444}
.pointer{left:785px;top:889px}
.author{left:748px;top:916px;width:221px;height:77px;background:#f8f8f4}
.author .portrait{left:5px;top:5px;width:62px;height:62px;border:1px solid #ddd;background:linear-gradient(160deg,#d8d4cc,#4a4540 60%,#1e1e1e)}
.author b{position:absolute;left:80px;top:12px;font-size:15px}
.author small{position:absolute;left:80px;top:38px;font-size:12.5px;color:#666;white-space:nowrap}
.footer{left:0;top:1062px;width:1250px;text-align:center;font-family:Arimo,sans-serif;font-size:12px;color:#555}
</style>
</head>
<body>
<svg class="backdrop" width="1200" height="1099" viewBox="0 0 1200 1099" role="img" aria-label="Blurred black and white city skyline photograph">
  <defs>
    <linearGradient id="city" x1="0" y1="0" x2="1" y2="1">
      <stop offset="0" stop-color="#7a7a7a"/><stop offset=".4" stop-color="#a5a5a5"/><stop offset=".7" stop-color="#6d6d6d"/><stop offset="1" stop-color="#9a9a9a"/>
    </linearGradient>
  </defs>
  <rect width="1200" height="620" fill="url(#city)"/>
  <path d="M0 490 Q300 560 600 545 T1200 520 V1099 H0Z" fill="#f2f2f2"/>
  <path d="M0 580 Q400 640 700 620 T1200 630 V1099 H0Z" fill="var(--page)"/>
</svg>
<svg class="sidebar-shape" width="1200" height="1099" viewBox="0 0 1200 1099">
  <path d="M102 67 L357 45 V1003 L102 980Z" fill="var(--side)"/>
  <path d="M384 45 Q740 30 1098 70 V1000 Q740 1020 384 1003Z" fill="var(--panel)"/>
</svg>

<div class="abs brand"><span class="brand-dot"></span><span class="brand-name">KT Amber Lantern</span></div>

<ul class="abs nav">
  <li class="active">Home</li><li>About Us</li><li>Services</li><li>Training</li><li>Contact</li>
</ul>

<h3 class="abs side-title" style="left:125px;top:547px">Get In Touch</h3>
<ul class="abs contact">
  <li><svg width="16" height="14"><path d="M1 8 L8 1 L15 8 H13 V14 H3 V8Z" fill="#888"/></svg><span>418 Lantern Row<br>City, Country</span></li>
  <li><svg width="16" height="14"><path d="M1 6 Q8 0 15 6 L13 8 L11 6 H5 L3 8Z M4 9 H12 V13 H4Z" fill="#888"/></svg><span>+1 555 208 41 67</span></li>
  <li><svg width="16" height="14"><rect x="1" y="4" width="14" height="9" fill="#888"/><rect x="4" y="1" width="8" height="4" fill="#888"/></svg><span>+1 555 208 41 67</span></li>
  <li><svg width="16" height="14"><rect x="1" y="2" width="14" height="10" fill="#888"/><path d="M1 2 L8 8 L15 2" stroke="#333" fill="none"/></svg><a href="#">info@amberlantern.net</a></li>
  <li><svg width="16" height="14"><circle cx="8" cy="7" r="6.5" fill="#888"/><circle cx="8" cy="7" r="2.5" fill="#333"/></svg><a href="#">help@amberlantern.net</a></li>
  <li><svg width="16" height="14"><path d="M1 3 L5 1 L11 3 L15 1 V11 L11 13 L5 11 L1 13Z" fill="#888"/></svg><a href="#">Find us on map</a></li>
</ul>

<h3 class="abs side-title" style="left:118px;top:809px">Text Widget</h3>
<p class="abs widget">Lorem ipsum dolor sit amet, consectetur adipiscing elit. Pellentesque non eleifend.</p>
<div class="abs social"><span></span><span></span><span></span><span></span><span></span></div>

<div class="abs hero" role="img" aria-label="Photo of a smiling woman raising her arms against a blue sky by the sea"></div>
<div class="abs hero-caption">
  <span class="l1">Believing <b>Life</b> Success</span>
  <span class="l2"><small>with</small> Positive Thinking!</span>
</div>
<div class="abs dots"><span></span><span class="on"></span><span></span><span></span></div>

<div class="abs box quote">
  <span class="mark" style="left:24px;top:10px">“</span>
  <p class="r1"><em>Setting Goals</em>Is The First In</p>
  <p class="r2">TURNING THE <em>IVISIBLE INTO VISIBLE</em></p>
  <span class="mark" style="left:548px;top:82px">”</span>
</div>

<section class="abs box about">
  <div class="portrait" style="left:11px;top:10px;width:100px;height:90px" role="img" aria-label="Portrait photo of coach Marcus Hale"></div>
  <p class="who">Marcus Hale<small>Follow Me on <b>Chirper</b></small></p>
  <h2>About Life <span>Coaching</span> Business</h2>
  <p class="lead">Ipsum is simply dummy text of the printing and typesetting industry.</p>
  <p class="body"><b>Lorem Ipsum has been the industry's standard dummy text ever since the 1500s, when an unknown printer took a galley of type and scrambled it to make a type</b> specimen book. It has survived not only five centuries, but also the leap into electronic typesetting, remaining essentially unchanged. It was popularised in the 1960s with the release of Lettrafold sheets containing Lorem Ipsum passages, and more recently with desktop publishing software like Pagewright Studio including versions of Lorem Ipsum. <span class="more">read more</span></p>
</section>

<section class="abs box articles">
  <h2>Recent <span>Articles</span></h2>
  <article class="post" style="top:54px">
    <div class="date"><b>12</b><span>Feb</span></div>
    <p class="txt">Consectetur Adipiscing Elit<br>Lorem ipsum dolor sit amet, consectetur adipiscing elit. Pellentesque non eleifend tellus. Ut dui ve...<span class="more" style="font-weight:400">read more</span></p>
  </article>
  <div class="sep"></div>
  <article class="post" style="top:155px">
    <div class="date"><b>9</b><span>Feb</span></div>
    <p class="txt">Consectetur Adipiscing Elit<br>Lorem ipsum dolor sit amet, consectetur adipiscing elit. Pellentesque non eleifend tellus. Ut dui ve...<span class="more" style="font-weight:400">read more</span></p>
  </article>
</section>

<h2 class="abs testi-title">Tesimonials</h2>
<blockquote class="abs box testi">Lorem Ipsum has been the industry's standard dummy text ever since the 1500s, when an unknown printer took a galley of type and scram<br>The Service here is great. I would highly recommend it solutions to anybody wanting</blockquote>
<svg class="abs pointer" width="26" height="26"><path d="M0 0 H26 L0 24Z" fill="#cfcfcf"/></svg>
<div class="abs author">
  <div class="portrait" role="img" aria-label="Portrait photo of Owen Pryce in a suit"></div>
  <b>Owen Pryce</b><small>CEO &amp; Founder - Brightfold</small>
</div>

<p class="abs footer">2014 © amber lantern. ALL Rights Reserved. Privacy Policy | Terms of Service</p>
</body>
</html>
```